A professional I.T consulting company requires a web design

Our company needs a fresh web design to help us drive our business forward. We are an Information Technology company who specialises in solutions based I.T delivery and consultations and who prides ourselves on our professional approach to business.

We would like a web site design from a designer who may be able to help us upload the site to WordPress and who may be interested in completing the "coding" section of the site (minimal coding). Although this is not essential to this project and won't factor into the decision making process.

A very thorough brief has been put together for this design project so very limited work is required in regards to content (the brief sets out all the content text - copy write material).

Please see the attached project documents for a copy of the brief

Target Market(s)

Please refer to the attached brief

Industry/Entity Type

Business

Requirements
Must have
• Please refer to the attached brief
Nice to have
Should not have

```html
<!DOCTYPE html>
<html lang="en">
<head>
<meta charset="utf-8">
<title>Korvex – Our Team</title>
<link href="https://fonts.googleapis.com/css2?family=Roboto:wght@300;400;500&display=swap" rel="stylesheet">
<style>
:root{
  --blue:#1d8fd6;
  --blue-dark:#1a6fae;
  --nav:#2a86c8;
  --nav-active:#1d6aa4;
  --page:#f1f1f1;
  --band:#e6e6e6;
  --text:#8a8a8a;
  --line:#dcdcdc;
  --footer-text:#e6e6e6;
  --footer-line:#5a5a5a;
  --bar:#1f6aa8;
}
*{margin:0;padding:0;box-sizing:border-box}
html,body{width:846px;height:1200px;overflow:hidden}
body{position:relative;background:var(--page);font-family:"Roboto",Arial,sans-serif;color:var(--text)}
.abs{position:absolute}

/* header */
.brand{left:40px;top:24px}
.brand-name{font-size:32px;font-weight:500;color:var(--blue);letter-spacing:1px;line-height:1}
.brand-tag{font-size:8px;font-weight:400;letter-spacing:2px;color:#9a9a9a;margin-top:4px}
.social{display:flex;gap:5px}
.social span{width:22px;height:22px;border-radius:50%;display:block}
.social-top{left:693px;top:22px}
.social-top span{background:var(--blue-dark)}
.social-top span:last-child{background:#f08a1c}
.call{left:665px;top:56px;display:flex;gap:6px;align-items:center}
.call-icon{width:26px;height:27px;border-radius:3px;background:var(--blue);display:flex;align-items:center;justify-content:center}
.call-label{font-size:9px;letter-spacing:1.5px;color:#8a8a8a}
.call-number{font-size:15.5px;letter-spacing:1px;color:var(--blue)}

/* nav */
.nav{left:0;top:96px;width:846px;height:31px;background:linear-gradient(var(--nav),#2378b8);border-bottom:2px solid #1b5f94}
.nav a{position:absolute;top:0;height:31px;line-height:31px;font-size:10px;letter-spacing:1px;color:#fff;text-decoration:none}
.nav a.active{background:var(--nav-active);padding:0 8px}
.search{left:648px;top:100px;width:113px;height:24px;background:#fff;border:1px solid #d0d0d0;font-size:10.5px;color:#b0b0b0;padding:5px 9px;letter-spacing:.5px}
.search-btn{left:761px;top:100px;width:41px;height:24px;background:#1c5f97;display:flex;align-items:center;justify-content:center}

/* team */
.heading{left:59px;top:151px;font-size:19px;font-weight:400;color:var(--blue);display:flex;align-items:center;gap:8px}
.rule{left:59px;top:177px;width:688px;height:1px;background:var(--line)}
.rule-accent{left:59px;top:176px;width:68px;height:2px;background:var(--blue)}
.band{left:59px;top:428px;width:701px;height:199px;background:var(--band)}
.member .photo{width:131px;height:131px;border:4px solid #c9c9c9}
.member .name{width:131px;text-align:center;font-size:11px;color:var(--blue);margin-top:10px}
.member .role{width:131px;text-align:center;font-size:9.5px;color:var(--blue-dark);margin-top:3px}
.bio{left:218px;width:529px;font-size:12.4px;font-weight:300;line-height:18.3px;text-align:justify;color:#8c8c8c}
.bio p+p{margin-top:18.3px}
.rule-end{left:59px;top:852px;width:688px;height:1px;background:var(--line)}

/* footer */
.footer{left:0;top:902px;width:846px;height:269px;background:linear-gradient(#444,#333)}
.f-head{top:930px;font-size:12px;font-weight:400;letter-spacing:1.3px;color:var(--footer-text)}
.f-rule{height:1px;background:var(--footer-line)}
.quote{left:71px;display:flex;gap:11px;width:281px}
.quote .thumb{width:72px;height:71px;border:4px solid #2a2a2a;flex:none}
.quote p{font-size:8.6px;font-weight:300;letter-spacing:.6px;line-height:12.4px;color:#d6d6d6;text-align:justify}
.quote .by{color:var(--blue);display:block}
.links{left:414px;top:964px;list-style:none}
.links li{font-size:11px;letter-spacing:1px;color:var(--footer-text);height:24px}
.links li::before{content:"›";margin-right:9px;color:#ccc}
.loc{left:627px;font-size:10px;letter-spacing:1px;color:var(--footer-text);display:flex;gap:8px;line-height:13.5px}
.loc svg{flex:none;margin-top:1px}
.social-foot{left:631px;top:1070px}
.social-foot span{background:#ddd}
.bar{left:0;top:1171px;width:846px;height:29px;background:var(--bar);font-size:8.5px;font-weight:300;letter-spacing:.8px;color:#fff}
</style>
</head>
<body>

<header>
  <div class="abs brand">
    <div class="brand-name">KORVEX</div>
    <div class="brand-tag">CLEAR THINKING. SOLID DELIVERY</div>
  </div>
  <div class="abs social social-top" aria-label="Social links"><span></span><span></span><span></span><span></span></div>
  <div class="abs call">
    <div class="call-icon"><svg width="14" height="16" viewBox="0 0 14 16"><path d="M3 1l3 3-2 2c1 2 3 4 5 5l2-2 3 3-2 3C6 14 0 8 1 3z" fill="#fff"/></svg></div>
    <div>
      <div class="call-label">CALL US TOLL FREE</div>
      <div class="call-number">1300 555 019</div>
    </div>
  </div>
</header>

<nav class="abs nav">
  <a style="left:46px">HOME</a>
  <a class="active" style="left:95px">ABOUT US</a>
  <a style="left:183px">WHY KORVEX?</a>
  <a style="left:278px">SERVICES</a>
  <a style="left:355px">SOLUTIONS</a>
  <a style="left:442px">TECHNOLOGIES</a>
  <a style="left:553px">CONTACT</a>
</nav>
<div class="abs search">Search</div>
<div class="abs search-btn"><svg width="15" height="15" viewBox="0 0 15 15"><circle cx="5.5" cy="5.5" r="4" stroke="#fff" stroke-width="2" fill="none"/><path d="M8.5 8.5L13.5 13.5" stroke="#fff" stroke-width="2.5"/></svg></div>

<main>
  <h1 class="abs heading">OUR TEAM
    <svg width="22" height="14" viewBox="0 0 22 14"><circle cx="6" cy="4" r="3" fill="#1a6fae"/><circle cx="16" cy="4" r="3" fill="#1a6fae"/><circle cx="11" cy="5" r="3.4" fill="#1a6fae"/><path d="M1 13c0-4 3-5 5-5s5 1 5 5zM11 13c0-4 3-5 5-5s5 1 5 5z" fill="#1a6fae"/><path d="M5 14c0-4 3-6 6-6s6 2 6 6z" fill="#1a6fae"/></svg>
  </h1>
  <div class="abs rule"></div>
  <div class="abs rule-accent"></div>

  <div class="abs band"></div>

  <section class="abs member" style="left:67px;top:207px">
    <div class="photo" role="img" aria-label="Portrait photo of Alan Pryce" style="background:linear-gradient(135deg,#5a5048,#2c2a2c)"></div>
    <div class="name">Alan Pryce</div>
    <div class="role">Director</div>
  </section>
  <div class="abs bio" style="top:203px">
    <p>Our consultants are highly focused and committed to customer service and satisfaction and work hard to create lasting relationships with all we come into contact with. We pride ourselves on our personal investment into finding the right solution for our clients and in offering them a support network that is more akin to a personal relationship rather than a business partnership.</p>
    <p>Korvex has been built on a solid reputation for our professionalism and our no-nonsense approach to meeting the challenges presented by our clients ongoing needs and support requirements and have done so through the expert delivery of services by our qualified and highly trained technicians.</p>
    <p>Rest assured, that when you’re dealing with Korvex you’re dealing with someone who cares!</p>
  </div>

  <section class="abs member" style="left:67px;top:449px">
    <div class="photo" role="img" aria-label="Portrait photo of Dean Pryce" style="background:linear-gradient(135deg,#8a8a88,#3a3d48)"></div>
    <div class="name">Dean Pryce</div>
    <div class="role">Service Desk Coordinator</div>
  </section>
  <div class="abs bio" style="top:445px">
    <p>In 2013 Dean was selected to join Korvex due to his incredible focus on people and his absolute passion for helping others overcome their problems. It’s this attitude that sets Dean above the rest and allows him to offer our clients the very best in personalised services.</p>
    <p>Dean’s skillset effortlessly transitioned into his new role at Korvex; his strong customer focus and a well-grounded approach to problem solving has ensured Korvex deliver on what we promise. “Clear Thinking. Solid Delivery”.</p>
  </div>

  <section class="abs member" style="left:67px;top:657px">
    <div class="photo" role="img" aria-label="Portrait photo of Sam Ellis" style="background:linear-gradient(135deg,#6a4a34,#1e1e20)"></div>
    <div class="name">Sam Ellis</div>
    <div class="role">Senior Support Engineer</div>
  </section>
  <div class="abs bio" style="top:653px">
    <p>Sam too joined Korvex in 2013. Sam’s extraordinary caring nature caught Alan’s attention early in his career. Sam is a perfect fit for the Korvex’s culture; His ability to listen and understand the needs of client’s, his responsive personality and uncanny ability to translate often complex tasks into simple solutions has seen him excel thought his career.</p>
    <p>Sam’s IT career started in 2008 as an IT trainee in the health sector. His thirst for knowledge and commitment to helping others sore him well made him highly desirable in the private IT sector. In 2010 Sam established himself in the private sector as a leading solutions integrator and now has over 3 years’ experience delivering complex IT solutions.</p>
  </div>
  <div class="abs rule-end"></div>
</main>

<footer>
  <div class="abs footer"></div>

  <h2 class="abs f-head" style="left:70px">TESTIMONIALS</h2>
  <div class="abs f-rule" style="left:70px;top:951px;width:282px"></div>
  <div class="abs quote" style="top:964px">
    <div class="thumb" role="img" aria-label="Photo of Peter Haldane" style="background:linear-gradient(135deg,#f4f4f4,#9a8a80)"></div>
    <p>The staff at Korvex are the most enthusiastic and personable people I have met and have an extensive IT knowledge and thirst for greater knowledge <span class="by">- PETER HALDANE,</span></p>
  </div>
  <div class="abs f-rule" style="left:70px;top:1047px;width:282px"></div>
  <div class="abs quote" style="top:1058px">
    <div class="thumb" role="img" aria-label="Photo of Daniel Ostrowski" style="background:linear-gradient(135deg,#c4a27a,#3a3a3a)"></div>
    <p>The staff at Korvex are the most enthusiastic and personable people I have met and has an extensive IT knowledge and thirst for greater knowledge. <span class="by">- DANIEL OSTROWSKI,</span></p>
  </div>
  <div class="abs f-rule" style="left:70px;top:1139px;width:282px"></div>
  <div class="abs" style="left:75px;top:1149px;font-size:9.5px;letter-spacing:1px;color:var(--footer-text)">VIEW ALL</div>

  <h2 class="abs f-head" style="left:401px">QUICKLINKS</h2>
  <div class="abs f-rule" style="left:398px;top:951px;width:164px"></div>
  <ul class="abs links">
    <li>Home</li><li>About us</li><li>Why Korvex?</li><li>Services</li><li>Solutions</li><li>Technologies</li>
  </ul>
  <div class="abs f-rule" style="left:398px;top:1139px;width:164px"></div>

  <h2 class="abs f-head" style="left:625px">LOCATION</h2>
  <div class="abs f-rule" style="left:625px;top:951px;width:160px"></div>
  <div class="abs loc" style="top:964px">
    <svg width="14" height="13" viewBox="0 0 14 13"><path d="M7 0L0 6h2v7h10V6h2z" fill="#ddd"/></svg>
    <div>2181 HARBOUR LANE<br>RIVERSIDE, CA<br>92501</div>
  </div>
  <div class="abs loc" style="top:1012px">
    <svg width="14" height="13" viewBox="0 0 14 13"><path d="M10 0l3 3-1 2C9 9 6 12 2 13L0 10l3-2 2 1c1-1 3-3 4-5L8 2z" fill="#ddd"/></svg>
    <div>1300 555 019</div>
  </div>
  <div class="abs loc" style="top:1035px">
    <svg width="15" height="11" viewBox="0 0 15 11"><rect width="15" height="11" fill="#ddd"/><path d="M0 0l7.5 6L15 0" stroke="#555" fill="none"/></svg>
    <div>hello@korvex.example</div>
  </div>
  <div class="abs social social-foot" aria-label="Social links"><span></span><span></span><span></span><span></span></div>

  <div class="abs bar">
    <span class="abs" style="left:67px;top:9px">Copyright 2014 · All rights reserved</span>
    <span class="abs" style="right:55px;top:9px">Sitemap &nbsp; &nbsp;| &nbsp; &nbsp;FAQ &nbsp; &nbsp;| &nbsp; &nbsp;Privacy Policy</span>
  </div>
</footer>

</body>
</html>
```